I need a new business card design for my pharmacy.

I need a business card design. I will include my logo.
The card needs to be readable. I prefer to have my logo on one side along with my website, the other side includes the other information. Please use combination of black, neon green, white, and silver. This needs to catch the eye but yet be clearly visible and legible. Thanks

Industry/Entity Type

Pharmacy

Contact Information for Business Card

It needs to have the following information listed:
Mel's Apothecary Owner/Pharm D.
7134 North Brook Lane
Sioux Falls, SD 57231
Phone 605-318-6207
Fax 605-318-6209
email: mel@melsapothecary-example.com
www.melsapothecary-example.com
Store hours Monday-Friday 8 am- 7 pm
Saturday 8 am- 12 pm
Sunday Closed
Please utilize the colors black, white, and neon green, maybe silver.

Requirements
Must have
• It needs to be easily readable!
Nice to have
• It should catch the eye.
Should not have
• Do not use any other colors except listed: black, neon green, white, & silver.

```html
<!DOCTYPE html>
<html lang="en">
<head>
<meta charset="utf-8">
<title>Mel's Apothecary – Business Card</title>
<link rel="stylesheet" href="https://fonts.googleapis.com/css2?family=Open+Sans:wght@400;700&family=Oswald:wght@300;600&display=swap">
<style>
  :root {
    --neon: #39ff14;
    --white: #ffffff;
    --silver: #c3c4c6;
    --black: #1c1c1c;
    --ink: #3a3a3a;
    --backdrop: #e9e9e9;
  }
  * { box-sizing: border-box; margin: 0; padding: 0; }
  html, body {
    width: 1200px; height: 1000px; overflow: hidden;
    background: var(--backdrop);
    font-family: "Open Sans", Arial, sans-serif;
  }
  .stage {
    position: relative; width: 1200px; height: 1000px;
    display: flex; flex-direction: column; align-items: center; justify-content: center; gap: 60px;
  }
  .card {
    position: relative; width: 700px; height: 400px;
    box-shadow: 0 6px 18px rgba(0,0,0,.18);
    overflow: hidden;
  }

  /* Front */
  .card-front { background: var(--neon); }
  .front-band {
    position: absolute; left: 0; top: 150px; width: 430px; height: 175px;
    background: var(--white);
    display: flex; align-items: center; justify-content: center; gap: 16px;
  }
  .front-band .mark {
    width: 30px; height: 30px; border-radius: 50%; background: var(--black);
  }
  .front-band .brand-name {
    font-weight: 700; font-size: 40px; color: var(--black); letter-spacing: -0.5px;
  }
  .front-web {
    position: absolute; left: 455px; top: 70px;
    font-size: 13px; color: var(--black);
  }
  .front-sign {
    position: absolute; right: 24px; bottom: 24px;
    display: flex; align-items: center; gap: 8px;
  }
  .front-sign .mark {
    width: 14px; height: 14px; border-radius: 50%; border: 2px solid var(--white);
  }
  .front-sign .brand-name { font-weight: 700; font-size: 14px; color: var(--white); }

  /* Back */
  .card-back { background: var(--silver); }
  .contact-list {
    position: absolute; left: 48px; top: 60px;
    list-style: none; font-size: 20px; line-height: 31px; color: var(--white);
  }
  .contact-list .label { display: inline-block; width: 44px; }
  .contact-list .indent { padding-left: 44px; }
  .owner {
    position: absolute; right: 40px; top: 200px; text-align: right;
  }
  .owner .brand-name { font-weight: 700; font-size: 22px; color: var(--white); }
  .owner .title { font-size: 15px; color: var(--black); }
  .rule {
    position: absolute; left: 40px; right: 30px; top: 262px;
    height: 1px; background: var(--black);
  }
  .hours {
    position: absolute; left: 40px; top: 274px;
    font-family: "Oswald", "Arial Narrow", sans-serif; font-weight: 300;
    font-size: 17px; letter-spacing: 3px; text-transform: uppercase; color: var(--white);
  }
  .closed {
    position: absolute; right: 150px; top: 316px;
    font-family: "Oswald", "Arial Narrow", sans-serif; font-weight: 600;
    font-size: 18px; letter-spacing: 1.5px; text-transform: uppercase; color: var(--black);
  }
</style>
</head>
<body>
<main class="stage">
  <section class="card card-front" aria-label="Card front">
    <div class="front-web">www.melsapothecary-example.com</div>
    <div class="front-band">
      <span class="mark"></span>
      <span class="brand-name">Mel's Apothecary</span>
    </div>
    <div class="front-sign">
      <span class="mark"></span>
      <span class="brand-name">Mel's Apothecary</span>
    </div>
  </section>

  <section class="card card-back" aria-label="Card back">
    <ul class="contact-list">
      <li><span class="label">P :-</span>605-318-6207</li>
      <li><span class="label">F :-</span>605-318-6209</li>
      <li><span class="label">E :-</span>mel@melsapothecary-example.com</li>
      <li><span class="label">A :-</span>7134 North Brook Lane</li>
      <li class="indent">Sioux Falls, SD 57231</li>
    </ul>
    <div class="owner">
      <div class="brand-name">Mel's Apothecary</div>
      <div class="title">Owner/Pharm D.</div>
    </div>
    <div class="rule"></div>
    <div class="hours">Store hours - Monday - Friday 8 am - 7 pm | Saturday 8 am - 12 pm.</div>
    <div class="closed">Sunday Closed</div>
  </section>
</main>
</body>
</html>
```